Commercial Construction Interior Fitout company needs Logo and Business Cards

We need a logo and business card design. We specialise in Commercial Ceilings, Partitions, Plastering and Carpentry.

Company name: 7QX Commercial Interiors. Would like a professional looking card more than a fancy look. Gloss front preferably black pattern with Fluro Green and white text.

Will need:

Name
Position
Phone
Fax
Email
Postal Address
Web address
Updates

Thank you so much everyone for your efforts and fantastic designs..   If I didn't respond to everyone personally,  my apologises. 

Again, thanks all

R.M                               

Target Market(s)

Existing & New clients in the Construction Industry

Industry/Entity Type

Business

Requirements
Nice to have
• 7QX to be overlapped or made into some sort of Logo

```html
<!DOCTYPE html>
<html lang="en">
<head>
<meta charset="utf-8">
<title>7QX Commercial Interiors – Business Cards</title>
<link rel="stylesheet" href="https://fonts.googleapis.com/css2?family=Arimo:wght@400;700&display=swap">
<style>
  :root {
    --canvas-bg: #e4e4e2;
    --card-black: #1c1b1b;
    --card-white: #ffffff;
    --brand-green: #45ad2f;
    --fluro-green: #3fcf3a;
    --ink: #1a1a1a;
    --ink-soft: #6b6b6b;
  }
  * { box-sizing: border-box; margin: 0; padding: 0; }
  html, body { width: 1200px; height: 900px; overflow: hidden; }
  body {
    background: var(--canvas-bg);
    font-family: "Arimo", Arial, sans-serif;
    position: relative;
  }
  .card {
    position: absolute;
    left: 300px;
    width: 600px;
    height: 345px;
    overflow: hidden;
    box-shadow: 0 6px 18px rgba(0,0,0,0.18);
  }

  /* Front */
  .card--front { top: 50px; background: var(--card-black); }
  .grid-band { position: absolute; left: 0; width: 100%; }
  .grid-band--ceiling {
    top: 0; height: 78px;
    background: linear-gradient(180deg, rgba(63,207,58,0.55) 0%, rgba(63,207,58,0.18) 70%, rgba(63,207,58,0) 100%);
  }
  .grid-band--floor {
    bottom: 0; height: 44px;
    background: linear-gradient(0deg, rgba(63,207,58,0.5) 0%, rgba(63,207,58,0.15) 70%, rgba(63,207,58,0) 100%);
  }
  .brand-lockup {
    position: absolute;
    left: 0; right: 0; top: 118px;
    text-align: center;
    color: var(--card-white);
    font-weight: 400;
  }
  .brand-lockup__name { font-size: 76px; line-height: 1; letter-spacing: 1px; }
  .brand-lockup__tagline { font-size: 22px; line-height: 1.2; margin-top: 8px; }

  /* Back */
  .card--back { top: 470px; background: var(--card-white); }
  .green-band { position: absolute; inset: 0; }
  .brand-mini {
    position: absolute;
    right: 26px; top: 26px;
    text-align: center;
    color: var(--ink);
    font-weight: 400;
  }
  .brand-mini__name { font-size: 50px; line-height: 1; }
  .brand-mini__tagline { font-size: 15px; line-height: 1.2; margin-top: 8px; }
  .holder { position: absolute; left: 36px; top: 106px; }
  .holder__name { font-size: 26px; line-height: 1.2; color: var(--ink); }
  .holder__role { font-size: 17px; line-height: 1.2; color: var(--ink-soft); margin-top: 6px; }
  .contact-list {
    position: absolute; left: 36px; top: 212px;
    font-size: 17px; color: var(--ink); line-height: 24px;
    display: grid; grid-template-columns: 70px auto;
  }
  .web-address { position: absolute; left: 36px; top: 304px; font-size: 17px; line-height: 24px; color: var(--ink); }
  .postal-address {
    position: absolute; left: 410px; top: 228px;
    font-size: 17px; color: var(--ink); line-height: 24px;
    white-space: nowrap;
  }
  .grid-band--floor-light {
    bottom: 0; height: 48px;
    background: linear-gradient(0deg, rgba(170,170,170,0.45) 0%, rgba(200,200,200,0.18) 70%, rgba(255,255,255,0) 100%);
  }
</style>
</head>
<body>
  <section class="card card--front" aria-label="Business card front">
    <div class="grid-band grid-band--ceiling" role="img" aria-label="Fluro green perspective ceiling grid pattern"></div>
    <div class="brand-lockup">
      <div class="brand-lockup__name">7QX</div>
      <div class="brand-lockup__tagline">Commercial Interiors</div>
    </div>
    <div class="grid-band grid-band--floor" role="img" aria-label="Fluro green perspective floor grid pattern"></div>
  </section>

  <section class="card card--back" aria-label="Business card back">
    <svg class="green-band" width="600" height="345" viewBox="0 0 600 345" aria-hidden="true">
      <polygon points="0,0 600,0 600,80 0,58" fill="var(--brand-green)"/>
    </svg>
    <div class="grid-band grid-band--floor-light" role="img" aria-label="Light grey perspective floor grid pattern"></div>
    <div class="brand-mini">
      <div class="brand-mini__name">7QX</div>
      <div class="brand-mini__tagline">Commercial Interiors</div>
    </div>
    <div class="holder">
      <div class="holder__name">Sam Carter</div>
      <div class="holder__role">Marketing Manager</div>
    </div>
    <div class="contact-list">
      <span>ph.</span><span>: (013) 456-789</span>
      <span>fax.</span><span>: (013) 456-789</span>
      <span>e-mail</span><span>: sam@7qxmail.com</span>
    </div>
    <div class="web-address">www.7qxcinteriors.com</div>
    <div class="postal-address">14 Quay Road, Milton<br>Eastvale, Northland<br>Zip 204817</div>
  </section>
</body>
</html>
```